Marrowind Lake Billboard

Looking to design a multi purpose billboard promoting Marrowind Lake as a destination point. Billboard size is 12ft x 40ft
My goal is to advertise our restaurant The Driftmill (pic attached)
What makes Marrowind a destination? It offers lodging / water skiing / Off Road Adventure / Camping / Fishing / Hunting
Want a catch phrase, something like "Looking For a Getaway" or "Need a Break"
Needs to really pop and catch the interest of the looker
maybe have our website address www.marrowinddriftmill.example
Open for ideas

```html
<!DOCTYPE html>
<html lang="en">
<head>
<meta charset="utf-8">
<title>Marrowind Lake Billboard – The Driftmill</title>
<link rel="stylesheet" href="https://fonts.googleapis.com/css2?family=Russo+One&family=Montserrat:wght@700&display=swap">
<style>
  :root {
    --page-bg: #e9ecef;
    --night: #110e0d;
    --sunset-orange: #e0783a;
    --sunset-rose: #c8645a;
    --dusk-purple: #5b3a3e;
    --forest: #23301f;
    --timber: #5a3a22;
    --band-orange: #f39a1f;
    --band-orange-light: #f7a935;
    --ink: #1a1410;
    --white: #ffffff;
    --outline-orange: #e58a1c;
  }
  * { margin: 0; padding: 0; box-sizing: border-box; }
  html, body {
    width: 1200px;
    height: 1160px;
    overflow: hidden;
    background: var(--page-bg);
  }
  .billboard {
    position: absolute;
    left: 0;
    top: 401px;
    width: 1200px;
    height: 358px;
    overflow: hidden;
    background:
      linear-gradient(90deg, var(--night) 0%, var(--night) 18%, rgba(17,14,13,0) 40%),
      linear-gradient(180deg, #7a4a52 0%, var(--sunset-rose) 28%, var(--sunset-orange) 48%, #a24a34 70%, var(--dusk-purple) 100%);
  }
  .scene-store {
    position: absolute;
    right: 0;
    top: 0;
    width: 470px;
    height: 260px;
    background:
      linear-gradient(180deg, var(--forest) 0%, rgba(35,48,31,0.6) 30%, rgba(90,58,34,0.85) 60%, var(--timber) 100%);
    -webkit-mask-image: linear-gradient(90deg, transparent 0%, #000 35%);
            mask-image: linear-gradient(90deg, transparent 0%, #000 35%);
  }
  .band {
    position: absolute;
    left: 0;
    bottom: 0;
    width: 1200px;
    height: 180px;
  }
  .brand {
    position: absolute;
    left: 40px;
    top: 56px;
    width: 150px;
    text-align: center;
    color: var(--white);
    font-family: "Montserrat", sans-serif;
    font-weight: 700;
    line-height: 1.1;
  }
  .brand-the { font-size: 15px; letter-spacing: 2px; }
  .brand-name { font-size: 22px; letter-spacing: 1px; }
  .brand-sub { font-size: 12px; letter-spacing: 1.5px; }
  .headline {
    position: absolute;
    left: 0;
    top: 0;
    width: 1200px;
    height: 190px;
    font-family: "Russo One", sans-serif;
    font-weight: 400;
    color: var(--white);
    -webkit-text-stroke: 4px var(--outline-orange);
    paint-order: stroke fill;
    text-shadow: 0 3px 6px rgba(0,0,0,0.45);
    text-transform: uppercase;
  }
  .headline-line {
    position: absolute;
    white-space: nowrap;
    line-height: 1;
    transform: skewX(-10deg);
    transform-origin: left bottom;
  }
  .headline-line--top { left: 294px; top: 36px; font-size: 66px; letter-spacing: 4px; }
  .headline-line--bottom { left: 400px; top: 110px; font-size: 76px; letter-spacing: 5px; }
  .activity {
    position: absolute;
    border-radius: 50%;
    border: 5px solid var(--white);
    box-shadow: 0 3px 8px rgba(0,0,0,0.4);
  }
  .activity--wrap   { left: 35px;  top: 184px; width: 140px; height: 140px; background: radial-gradient(circle at 45% 45%, #d8a76a, #8a4a2a 70%, #5a2c1c); }
  .activity--ribs   { left: 195px; top: 193px; width: 122px; height: 122px; background: linear-gradient(180deg, #2b2624 0%, #c2531e 35%, #a34118 70%, #3a2a24 100%); }
  .activity--skiing { left: 329px; top: 205px; width: 110px; height: 110px; background: linear-gradient(180deg, #6f8a5a 0%, #c9d6dc 40%, #ffffff 65%, #9fb3bd 100%); }
  .activity--cabin  { left: 454px; top: 206px; width: 108px; height: 108px; background: linear-gradient(180deg, #b9c2c8 0%, #a58a6a 40%, #7d7a50 70%, #5f6a3a 100%); }
  .activity--hunting{ left: 635px; top: 205px; width: 110px; height: 110px; background: linear-gradient(180deg, #cdb58f 0%, #8f8a5c 50%, #4a4a30 100%); }
  .activity--offroad{ left: 759px; top: 206px; width: 108px; height: 108px; background: linear-gradient(180deg, #dbe3ea 0%, #8b9298 40%, #2a2f35 70%, #6d6a5a 100%); }
  .activity--camping{ left: 881px; top: 193px; width: 122px; height: 122px; background: linear-gradient(180deg, #6f9ad0 0%, #c6d4e0 40%, #8ca3c0 65%, #5a4e40 100%); }
  .activity--fishing{ left: 1022px; top: 175px; width: 140px; height: 140px; background: linear-gradient(180deg, #5f7a3c 0%, #8fa3a0 45%, #6a8596 70%, #4d5a3a 100%); }
  .website {
    position: absolute;
    left: 0;
    bottom: 6px;
    width: 1200px;
    text-align: center;
    font-family: "Montserrat", sans-serif;
    font-weight: 700;
    font-size: 17px;
    letter-spacing: 8.4px;
    color: var(--ink);
  }
</style>
</head>
<body>
  <main class="billboard">
    <div class="scene-store" role="img" aria-label="Photo of the Driftmill general store and bait shop at dusk, with trees behind"></div>
    <svg class="band" viewBox="0 0 1200 180" aria-hidden="true">
      <defs>
        <linearGradient id="bandFill" x1="0" y1="0" x2="0" y2="1">
          <stop offset="0" stop-color="#f7a935"/>
          <stop offset="1" stop-color="#f39a1f"/>
        </linearGradient>
      </defs>
      <path d="M0 14 C 220 -2, 420 52, 640 58 C 860 62, 1020 18, 1200 30 L1200 180 L0 180 Z" fill="url(#bandFill)"/>
    </svg>

    <div class="brand">
      <div class="brand-the">THE</div>
      <div class="brand-name">DRIFTMILL</div>
      <div class="brand-sub">GENERAL STORE</div>
    </div>

    <h1 class="headline">
      <span class="headline-line headline-line--top">Looking for a</span>
      <span class="headline-line headline-line--bottom">Getaway</span>
    </h1>

    <div class="activity activity--wrap" role="img" aria-label="Photo of a grilled wrap with fries"></div>
    <div class="activity activity--ribs" role="img" aria-label="Photo of ribs on a grill"></div>
    <div class="activity activity--skiing" role="img" aria-label="Photo of water skiing on the lake"></div>
    <div class="activity activity--cabin" role="img" aria-label="Photo of a lodging cabin in the hills"></div>
    <div class="activity activity--hunting" role="img" aria-label="Photo of a hunter seated in a field"></div>
    <div class="activity activity--offroad" role="img" aria-label="Photo of an off-road vehicle"></div>
    <div class="activity activity--camping" role="img" aria-label="Photo of a tent at a mountain campsite"></div>
    <div class="activity activity--fishing" role="img" aria-label="Photo of fishing at the water's edge"></div>

    <p class="website">www.marrowinddriftmill.example</p>
  </main>
</body>
</html>
```